Business Card- Can you make it cool vs boring!

Need a refresh on my business card! Want it to be modern but simple, classic and a pop of coolness! we do senior living and it is boring. but that doesn't mean our business card have to look boring! Open to two sided cards. our website is www.Bruvel-HQ.com

Target Market(s)

capital market

Industry/Entity Type

senior housing/ real estate

Contact Information for Business Card

logo/ name/ cell/ address/ www.Bruvel-HQ.com/ space for a QR code

Requirements
Must have
• maybe a QR code (do not make prominent I may not use the QR so design where it can be taken out) that link to more about us/ landing page. needs to be modern but clean
Should not have
• clip art or script

```html
<!DOCTYPE html>
<html lang="en">
<head>
<meta charset="utf-8">
<title>Bruvel Living – Business Card</title>
<link rel="stylesheet" href="https://fonts.googleapis.com/css2?family=Saira:wght@400;500&display=swap">
<style>
  :root {
    --backdrop: #e4e4e4;
    --terracotta: #b95b34;
    --terracotta-deep: #8b3226;
    --rust: #b4522b;
    --paper: #ffffff;
    --ink-light: #ffffff;
  }
  * { box-sizing: border-box; margin: 0; padding: 0; }
  html, body {
    width: 1200px;
    height: 1200px;
    overflow: hidden;
    background: var(--backdrop);
  }
  .stage {
    position: relative;
    width: 1200px;
    height: 1200px;
    font-family: "Saira", sans-serif;
  }
  .card {
    position: absolute;
    left: 159px;
    width: 880px;
    height: 515px;
  }
  .card--front { top: 61px; background: var(--terracotta); }
  .card--back { top: 606px; background: var(--paper); }

  .brand-name {
    position: absolute;
    left: 0;
    right: 0;
    text-align: center;
    font-weight: 500;
    font-size: 84px;
    letter-spacing: 2px;
    line-height: 1;
  }
  .card--front .brand-name { top: 118px; color: var(--terracotta-deep); }
  .card--back .brand-name { top: 215px; color: var(--rust); }

  .divider {
    position: absolute;
    left: 79px;
    width: 724px;
    top: 302px;
    height: 2px;
    background: var(--terracotta-deep);
  }
  .contact-row {
    position: absolute;
    left: 79px;
    display: flex;
    align-items: flex-start;
    gap: 14px;
    color: var(--ink-light);
    font-size: 21px;
    line-height: 29px;
    font-weight: 400;
  }
  .contact-row--phone { top: 339px; }
  .contact-row--address { top: 398px; }
  .contact-icon { width: 26px; height: 26px; flex: none; margin-top: 1px; }
  .website {
    position: absolute;
    right: 77px;
    top: 429px;
    color: var(--terracotta-deep);
    font-size: 20px;
    font-weight: 500;
    letter-spacing: 2.5px;
  }
</style>
</head>
<body>
<main class="stage">
  <section class="card card--front">
    <h1 class="brand-name">Bruvel Living</h1>
    <div class="divider"></div>

    <p class="contact-row contact-row--phone">
      <svg class="contact-icon" viewBox="0 0 26 26" aria-hidden="true">
        <rect width="26" height="26" rx="4" fill="#fff"/>
        <path d="M8.5 5.5l3 3-1.8 2c1 2.2 2.6 3.8 4.8 4.8l2-1.8 3 3-2.2 2.3C12 18.2 7.8 14 6.2 8.7z" fill="#b95b34"/>
      </svg>
      <span>(555) 014-2870</span>
    </p>

    <p class="contact-row contact-row--address">
      <svg class="contact-icon" viewBox="0 0 26 26" aria-hidden="true">
        <rect width="26" height="26" rx="4" fill="#fff"/>
        <path d="M13 5a5.5 5.5 0 0 0-5.5 5.5C7.5 15 13 21 13 21s5.5-6 5.5-10.5A5.5 5.5 0 0 0 13 5zm0 7.7a2.2 2.2 0 1 1 0-4.4 2.2 2.2 0 0 1 0 4.4z" fill="#b95b34"/>
      </svg>
      <span>4410 Larkmoor Lane, Suite #2105<br>Cedar Hollow, TX 77501</span>
    </p>

    <p class="website">www.Bruvel-HQ.com</p>
  </section>

  <section class="card card--back">
    <h2 class="brand-name">Bruvel Living</h2>
  </section>
</main>
</body>
</html>
```